Letterhead Design Project

We are looking for a simple letterhead design that reflects our core purpose. We help our clients gain clarity and focus but we are there to help them execute. The letterhead design would mainly be utilised for engagement letters and contracts.

Target Market(s)

The customers of our business are large corporate organisations.

Requirements
Must have
• The letterhead must have the company logo
The font used must tie in to the font used in the company logo

Must have the following business details
Address: Level 10, 27 Harlow Lane, Melbourne, Australia, 3000
Phone: +61 3 527 948 183
Fax: +61 3 9042 5317
Website: www.bovrin-u.com.au
Twiiter: @bovrin_u

```html
<!DOCTYPE html>
<html lang="en">
<head>
<meta charset="utf-8">
<title>Bovrin-u Letterhead</title>
<link rel="stylesheet" href="https://fonts.googleapis.com/css2?family=Questrial&display=swap">
<style>
  :root {
    --backdrop: #46474b;
    --paper: #ffffff;
    --brand-blue: #0b59a6;
    --ink-light: #ffffff;
  }
  * { box-sizing: border-box; margin: 0; padding: 0; }
  html, body {
    width: 1200px;
    height: 849px;
    overflow: hidden;
    background: var(--backdrop);
  }
  .canvas {
    position: relative;
    width: 1200px;
    height: 849px;
    background: var(--backdrop);
    font-family: "Questrial", Arial, sans-serif;
  }
  .letterhead {
    position: absolute;
    left: 324px;
    top: 34px;
    width: 552px;
    height: 780px;
    background: var(--paper);
  }
  .brand-tab {
    position: absolute;
    left: 202px;
    top: 0;
    width: 146px;
    height: 56px;
    background: var(--brand-blue);
    display: flex;
    align-items: center;
    justify-content: center;
  }
  .brand-name {
    color: var(--ink-light);
    font-size: 27px;
    letter-spacing: 0.5px;
    font-weight: 400;
  }
  .footer-band {
    position: absolute;
    left: 0;
    bottom: 0;
    width: 100%;
    height: 64px;
    background: var(--brand-blue);
    color: var(--ink-light);
    font-size: 9.5px;
    line-height: 1.35;
  }
  .contact-left {
    position: absolute;
    left: 10px;
    bottom: 6px;
  }
  .contact-right {
    position: absolute;
    right: 10px;
    top: 6px;
    text-align: right;
  }
  .brand-seal {
    position: absolute;
    left: 306px;
    top: -14px;
    width: 44px;
    height: 44px;
  }
</style>
</head>
<body>
  <main class="canvas">
    <article class="letterhead">
      <header class="brand-tab">
        <span class="brand-name">Bovrin-u</span>
      </header>

      <footer class="footer-band">
        <svg class="brand-seal" viewBox="0 0 44 44" aria-hidden="true">
          <circle cx="22" cy="22" r="21" fill="var(--brand-blue)"/>
          <circle cx="22" cy="22" r="17.5" fill="none" stroke="var(--ink-light)" stroke-width="2"/>
        </svg>
        <address class="contact-left" style="font-style: normal;">
          <p>Phone: +61 3 527 948 183</p>
          <p>Fax: +61 3 9042 5317</p>
          <p>Address: Level 10, 27 Harlow Lane, Melbourne, Australia, 3000</p>
        </address>
        <address class="contact-right" style="font-style: normal;">
          <p>Website: www.bovrin-u.com.au</p>
          <p>Twitter: @bovrin_u</p>
        </address>
      </footer>
    </article>
  </main>
</body>
</html>
```